Analytics/BI tech start-up seeks sharp, creative, simple, secret agent type logo & theme

"Quarry 7 Technologies" seeks a logo design/color scheme template for NYC based tech start-up of software engineers, solutions architects, and data/BI analysts. We develop reporting solutions and analytics platforms for small-medium sized businesses. We code for database, cloud, and web/mobile apps.<br/><br/>Some *very basic, limited* sketches are attached to show ideas we've had. We need a logo and color scheme that may be used for business cards, paper letterhead and envelopes, and web pages to be published at "www.quarry7.dev".<br/><br/>We like the black/red, red/white, blue/black, white/black contrasts as a stating point, and prefer black background business cards, but open to anything if it feels like a good match. We are relying on the projects submitted here to take care of the creativity part of our image, which we work on logistics to launching our start-up. Something that could also be easily translated into black/white, grayscale would be appreciated as well. while log is important, we also need an icon that may be used as an app thumbnail. For font, we prefer all caps.<br/><br/>Business: Quarry 7 Technologies<br/>Slogan: If. Else. Us. / If -> Else -> Us / If - Else - Us / etc.<br/>Website: www.quarry.dev<br/>Icon: [Q7] , only as a starting point<br/>Theme Ideas: Sleek, futuristic, secret agent-like tech, simple, bold color contrasts, software code related<br/><br/>Feel free to reach out to jvorenko@mailbarn.example as a contact for any questions or follow up. We look forward to seeing amazing ideas!
Updates

We would like to provide the opportunity for as many different submissions as possible.

Target Market(s)

Small business owners, entrepreneurs, financial/tech companies, freelance engineers, people in need of IT assistance to elevate business

Industry/Entity Type

It Company

Contact Information for Business Card

Individual Info: Name, Position, Phone Number 1, Phone Number 2 (optional), Fax Number, email Address.
Company Info: Name, logo, icon (optional), web site, slogan

Font styles to use
Sans Serif
Other font styles liked:
• Similar to Biome Light All Caps, Hollow Meridian type style

Requirements
Must have
• Pronounced 1 in the logo, either in the word Section or not. Bold color contrast, one side with only logo or icon, possible web address too. Other side with all individual info plus logo, and/or icon and web address. If using uploaded files as a base, center the C more between the E and T, it is too closer to the T as is.
Nice to have
• Bolder font possibly, more square edged at ends of letters but still with minor curved corners. Icon suggested as a starting point is “[Q7]” and instead of a slogan, use "Data - Cloud - Web - Software" and the dividers don't necessary have to be hyphens.
Should not have
• Open to all creative ideas, try anything. Please come up with different logos than are in the attached files, they are meant as a starting point.

```html
<!DOCTYPE html>
<html lang="en">
<head>
<meta charset="utf-8">
<title>Quarry 7 Technologies – Business Card</title>
<link href="https://fonts.googleapis.com/css2?family=Open+Sans:wght@400;700&display=swap" rel="stylesheet">
<style>
  :root {
    --backdrop: #2a2a2a;
    --card: #1e1e1e;
    --accent: #5fc9d3;
    --ink: #f2f2f2;
    --deboss: #3a3a3a;
  }
  * { margin: 0; padding: 0; box-sizing: border-box; }
  html, body {
    width: 1200px; height: 900px; overflow: hidden;
    background: var(--backdrop);
    font-family: "Open Sans", Arial, sans-serif;
  }
  .card {
    position: absolute; left: 280px;
    width: 640px; height: 366px;
    background: var(--card);
    box-shadow: 0 14px 32px rgba(0,0,0,.55);
  }
  .card-front { top: 44px; }
  .card-back { top: 490px; }

  .brand { position: absolute; text-align: center; font-weight: 400; }
  .brand-name { line-height: 1; white-space: nowrap; }
  .brand-sub { white-space: nowrap; }

  .card-front .brand {
    left: 250px; top: 58px; width: 300px; color: var(--accent);
  }
  .card-front .brand-name { font-size: 44px; letter-spacing: 3px; }
  .card-front .brand-sub { font-size: 19px; letter-spacing: 5px; margin-top: 6px; }

  .card-back .brand {
    left: 0; right: 0; top: 120px; color: var(--deboss);
  }
  .card-back .brand-name { font-size: 64px; letter-spacing: 4px; }
  .card-back .brand-sub { font-size: 26px; letter-spacing: 8px; margin-top: 8px; }

  .person {
    position: absolute; right: 330px; top: 192px;
    text-align right; text-align: right; color: var(--ink);
  }
  .person-name {
    color: var(--accent); font-weight: 700; font-size: 18px;
    text-transform: uppercase; letter-spacing: .4px; white-space: nowrap;
  }
  .person-role { font-size: 14px; margin-bottom: 10px; }
  .person-address { font-size: 13px; line-height: 1.45; white-space: nowrap; }

  .divider {
    position: absolute; left: 328px; top: 192px;
    width: 2px; height: 124px; background: var(--accent);
  }
  .contacts {
    position: absolute; left: 346px; top: 194px;
    list-style: none; color: var(--ink); font-size: 13.5px;
  }
  .contacts li { display: flex; align-items: center; height: 24px; white-space: nowrap; }
  .contacts svg { width: 14px; height: 14px; margin-right: 7px; fill: var(--accent); flex: none; }
</style>
</head>
<body>
  <section class="card card-front">
    <div class="brand">
      <div class="brand-name">QUARRY 7</div>
      <div class="brand-sub">TECHNOLOGIES</div>
    </div>

    <div class="person">
      <div class="person-name">Dara Kellworth</div>
      <div class="person-role">President</div>
      <div class="person-address">4180 Ferrow Pier Road<br>Suite 12, Lowmere CA 90417</div>
    </div>

    <div class="divider"></div>

    <ul class="contacts">
      <li>
        <svg viewBox="0 0 24 24"><path d="M6.6 10.8a15 15 0 0 0 6.6 6.6l2.2-2.2c.3-.3.7-.4 1-.2 1.1.4 2.3.6 3.6.6.6 0 1 .4 1 1V20c0 .6-.4 1-1 1A17 17 0 0 1 3 4c0-.6.4-1 1-1h3.5c.6 0 1 .4 1 1 0 1.3.2 2.5.6 3.6.1.3 0 .7-.2 1z"/></svg>
        555-318-2704
      </li>
      <li>
        <svg viewBox="0 0 24 24"><path d="M6 2h10l2 2v4H6z M3 9h18v9h-3v4H6v-4H3z M8 15v5h8v-5z"/></svg>
        555-318-2704
      </li>
      <li>
        <svg viewBox="0 0 24 24"><path d="M7 1h10a2 2 0 0 1 2 2v18a2 2 0 0 1-2 2H7a2 2 0 0 1-2-2V3a2 2 0 0 1 2-2zm0 3v15h10V4z"/></svg>
        555-318-2704
      </li>
      <li>
        <svg viewBox="0 0 24 24"><path d="M2 5h20v14H2z M3 6l9 7 9-7" stroke="#1e1e1e" stroke-width="1.5"/></svg>
        info@quarry7technologies.example
      </li>
      <li>
        <svg viewBox="0 0 24 24"><circle cx="12" cy="12" r="10"/><path d="M2 12h20M12 2c3 3 3 17 0 20M12 2c-3 3-3 17 0 20" stroke="#1e1e1e" stroke-width="1.4" fill="none"/></svg>
        www.quarry7technologies.example
      </li>
    </ul>
  </section>

  <section class="card card-back">
    <div class="brand">
      <div class="brand-name">QUARRY 7</div>
      <div class="brand-sub">TECHNOLOGIES</div>
    </div>
  </section>
</body>
</html>
```